Wendorf Legal: Sole Practitioner Law Firm seeking corporate branding drawing on unique bush setting

I need a logo, stationary and business card design for my law firm. I will be practising as a sole practitioner specialising in corporate, commercial, finance, migration and agriculture law. Having left my corporate job in the city and relocated our family to our farm in regional Western Australia, I would like the corporate design for my company to be crisp, stylish, concise and uncomplicated. The law firm is called "Wendorf Legal" because we have a colony of the endangered Carnaby Black Cockatoos living in the bush behind our homestead (which is also my office). I will travel to clients rather than have them visit me. I would like to see a stylised image of the bird with some Australian native bush included in the design, either as a background image on the back of the card. A separate brief has been created for the logo and stationary though I hope all 3 pieces of work will "marry". The final design should communicate clarity of vision, efficiency, compassion and solution/ outcome focused. I prefer to have the business cards printed on card with a bit of texture and substance. I will try not to use laminated card as I consider it feels "plastic and commoditised" which is inconsistent with the image and feel of the business I intend creating. Please see attached brief for further details of the design brief.

Target Market(s)

Agriculture and Horticulture companies, Farmers, Family offices and estates, banks, insurance companies, individuals wishing to migrate to Australia

Industry/Entity Type

Legal

Contact Information for Business Card

Harriet Dunbar-Kelso
LLB (Hons), BSc., MEc.
Legal Practitioner and Director

WENDORF LEGAL PTY LTD
PO Box 273, Yarrowind WA 6057
Ph: 0472 918205
Email: harrietdk@quillnet.com

Solicitor admitted to practice in the Senior Bench Tribunal of Western Australia, England and Wales, NSW, and Registered Practitioner of the Apex Bench of Australia

Logo Text

WENDORF LEGAL: Client Focused Commercial Legal Solutions

Font styles to use
Other font styles liked:
• Verlag

Colors
ec1f27
fbee3d
9bcb3c
ffffff
1b1b1b
c4c4c4

Requirements
Must have
• A look and feel of quality, conservatism, adventure
Nice to have
• A stylised image of a Carnaby Cockatoo and Australian flora as a background image or design on the back of the card.
Should not have
• Clutter, cartoons

```html
<!DOCTYPE html>
<html lang="en">
<head>
<meta charset="utf-8">
<title>Wendorf Legal — Stationery</title>
<link rel="stylesheet" href="https://fonts.googleapis.com/css2?family=Open+Sans:wght@400;600&family=Oswald:wght@500&display=swap">
<style>
  :root{
    --red:#ec1f27;
    --yellow:#fbee3d;
    --green:#9bcb3c;
    --white:#ffffff;
    --ink:#1b1b1b;
    --grey:#c4c4c4;
    --text:#555555;
    --bg:#ecedef;
    --plum:#4a1f3a;
    --wine:#8c2137;
    --band-top:linear-gradient(90deg,var(--green) 0%,var(--yellow) 55%,#f39a1f 85%,var(--red) 100%);
    --band-bottom:linear-gradient(90deg,var(--red) 0%,#f39a1f 20%,var(--yellow) 55%,var(--green) 100%);
    --card-glow:linear-gradient(90deg,var(--green) 0%,#d6df3a 30%,var(--yellow) 48%,#f39a1f 72%,var(--red) 100%);
  }
  *{box-sizing:border-box;margin:0;padding:0}
  html,body{width:1200px;height:800px;overflow:hidden}
  body{background:var(--bg);font-family:"Open Sans",Arial,sans-serif;color:var(--text);position:relative}

  /* Letterhead */
  .letterhead{position:absolute;left:70px;top:50px;width:494px;height:700px;background:var(--white);box-shadow:0 2px 10px rgba(0,0,0,.12);overflow:hidden}
  .letterhead__band{height:9px}
  .letterhead__band--top{background:var(--band-top)}
  .letterhead__band--bottom{position:absolute;left:0;right:0;bottom:0;background:var(--band-bottom)}
  .letterhead__head{display:flex;justify-content:space-between;align-items:flex-start;padding:22px 34px 0}
  .brand{display:flex;align-items:center;gap:8px;font-size:22px;font-weight:600;color:var(--ink);border-bottom:1px solid var(--grey);padding-bottom:8px;width:170px}
  .brand__dot{width:12px;height:12px;border-radius:50%;background:var(--ink);flex:none}
  .letterhead__meta{font-size:6.5px;font-weight:600;color:#888;letter-spacing:.5px;line-height:1.5;margin-top:2px}
  .recipient{text-align:right;font-size:9px;font-weight:600;color:#777;line-height:1.35;padding:6px 34px 0}
  .salutation{font-size:11px;font-weight:600;color:#666;padding:10px 34px 0}
  .letter{padding:22px 34px 0;font-size:8.6px;line-height:1.65}
  .letter p{margin-bottom:14px}
  .signoff{padding:26px 34px 0;font-size:9px;color:#888}
  .signoff__name{margin-top:22px;font-size:11px;font-weight:600;color:#5a5aa0}
  .letterhead__foot{position:absolute;left:34px;right:34px;bottom:22px;border-top:1px solid var(--grey);padding-top:9px;display:flex;justify-content:space-between;font-size:8.5px;color:#888}
  .contact{display:flex;align-items:center;gap:5px}
  .contact svg{width:10px;height:10px;fill:#666}

  /* Business cards */
  .card{position:absolute;width:430px;height:250px;background:var(--white);box-shadow:0 2px 10px rgba(0,0,0,.14);overflow:hidden}
  .card--front{left:650px;top:80px}
  .card--back{left:650px;top:440px}
  .card__glow{position:absolute;left:0;right:0;top:0;height:160px;background:var(--card-glow)}
  .card__arc{position:absolute;left:95px;top:42px;width:240px;height:240px;border-radius:50%;background:var(--white)}
  .card__identity{position:absolute;left:95px;top:68px;width:240px;text-align:center}
  .card__name{font-family:"Oswald",Arial,sans-serif;font-weight:500;font-size:20px;color:var(--ink);letter-spacing:.3px}
  .card__quals{font-family:"Oswald",Arial,sans-serif;font-size:9.5px;letter-spacing:2.4px;color:#555;margin-top:3px}
  .card__role{font-family:"Oswald",Arial,sans-serif;font-size:8px;letter-spacing:1.8px;color:#555;margin-top:3px}
  .card__details{position:absolute;left:22px;right:22px;top:172px;display:flex;justify-content:space-between;font-size:9px;line-height:1.5;color:#666}
  .card__details .contact{align-items:flex-start}
  .card__details .stack{display:flex;flex-direction:column;gap:6px}

  .card__artwork{position:absolute;inset:0;background:radial-gradient(circle at 20% 30%,var(--wine) 0%,var(--plum) 55%,#2a1224 100%)}
  .card__seal{position:absolute;left:125px;top:30px;width:190px;height:190px;border-radius:50%;background:var(--white);display:flex;flex-direction:column;align-items:center;justify-content:center;text-align:center;padding:0 18px}
  .card__seal .brand{border:none;width:auto;font-size:22px;padding:0}
  .card__admission{font-size:6.6px;line-height:1.45;color:var(--ink);margin-top:10px}
</style>
</head>
<body>

<article class="letterhead">
  <div class="letterhead__band letterhead__band--top"></div>
  <header class="letterhead__head">
    <div class="brand"><span class="brand__dot"></span>Wendorf Legal</div>
    <div class="letterhead__meta">HARRIET DUNBAR-KELSO<br>WENDORF LEGAL PTY LTD<br>ABN 00 000 000 000</div>
  </header>
  <address class="recipient" style="font-style:normal">Owen Halloway<br>Fernleaf Studio<br>Level 3, 9 Ridge St<br>Bramwell NSW 2031<br>Australia</address>
  <p class="salutation">Dear Mr. Halloway</p>
  <div class="letter">
    <p>Lorem ipsum dolor sit amet, consectetur adipiscing elit. Vestibulum adipiscing felis ac tortor consectetur feugiat. Etiam malesuada sodales eros ut ornare. Sed lorem eros, mattis id pretium ut, faucibus sit amet quam. Nullam consectetur ultricies ipsum, fringilla porttitor erat ornare at. Sed sit amet dui vel sapien ultrices vulputate. In hac habitasse platea dictumst. Nam est nisi, rhoncus at sagittis a, porttitor adipiscing nulla. Vivamus placerat felis ultrices quam iaculis eget dignissim felis egestas. Integer nec molestie lorem. Sed odio tellus, vulputate sed laoreet non, vulputate id justo. Etiam suscipit, odio vel auctor dictum, felis turpis ullamcorper neque, quis sodales metus in magna. Morbi pellentesque justo et quam laoreet facilisis.</p>
    <p>Class aptent taciti sociosqu ad litora torquent per conubia nostra, per inceptos himenaeos. Pharetra fermentum, urna tortor iaculis erat, vitae sollicitudin leo mauris quis sagittis ultrices. Mauris fermentum porttitor nisi, eu facilisis lorem consectetur euismod id, scelerisque viverra odio. Nullam scelerisque metus in dolor. Quisque dignissim mauris a neque luctus hendrerit eu, interdum eu nulla. Curabitur a velit metus eget felis eleifend adipiscing.</p>
    <p>Pretium mauris suscipit nunc, sed tempor ante lectus vel nisl.</p>
  </div>
  <div class="signoff">Yours sincerely
    <div class="signoff__name">H. Dunbar-Kelso</div>
  </div>
  <footer class="letterhead__foot">
    <span class="contact"><svg viewBox="0 0 10 10"><path d="M5 0a3.5 3.5 0 0 0-3.5 3.5C1.5 6 5 10 5 10s3.5-4 3.5-6.5A3.5 3.5 0 0 0 5 0zm0 5a1.5 1.5 0 1 1 0-3 1.5 1.5 0 0 1 0 3z"/></svg>PO Box 273, Yarrowind WA 6057</span>
    <span class="contact"><svg viewBox="0 0 10 10"><circle cx="5" cy="5" r="4.5" fill="none" stroke="#666"/><path d="M.5 5h9M5 .5c-2.5 3-2.5 6 0 9M5 .5c2.5 3 2.5 6 0 9" fill="none" stroke="#666" stroke-width=".7"/></svg>harrietdk@quillnet.com</span>
    <span class="contact"><svg viewBox="0 0 10 10"><path d="M2 .5 3.8 2.8 2.9 4c.7 1.4 1.7 2.4 3.1 3.1l1.2-.9L9.5 8 8.4 9.5C4.4 9.2.8 5.6.5 1.6z"/></svg>0472 918205</span>
  </footer>
  <div class="letterhead__band letterhead__band--bottom"></div>
</article>

<section class="card card--front">
  <div class="card__glow"></div>
  <div class="card__arc"></div>
  <div class="card__identity">
    <div class="card__name">HARRIET DUNBAR-KELSO</div>
    <div class="card__quals">LLB (HONS), BSC., MEC.</div>
    <div class="card__role">LEGAL PRACTITIONER AND DIRECTOR</div>
  </div>
  <div class="card__details">
    <span class="contact"><svg viewBox="0 0 10 10"><path d="M5 0a3.5 3.5 0 0 0-3.5 3.5C1.5 6 5 10 5 10s3.5-4 3.5-6.5A3.5 3.5 0 0 0 5 0zm0 5a1.5 1.5 0 1 1 0-3 1.5 1.5 0 0 1 0 3z"/></svg><span>WENDORF LEGAL PTY LTD<br>PO Box 273, Yarrowind WA 6057</span></span>
    <div class="stack">
      <span class="contact"><svg viewBox="0 0 10 10"><path d="M2 .5 3.8 2.8 2.9 4c.7 1.4 1.7 2.4 3.1 3.1l1.2-.9L9.5 8 8.4 9.5C4.4 9.2.8 5.6.5 1.6z"/></svg>0472 918205</span>
      <span class="contact"><svg viewBox="0 0 10 10"><circle cx="5" cy="5" r="4.5" fill="none" stroke="#666"/><path d="M.5 5h9M5 .5c-2.5 3-2.5 6 0 9M5 .5c2.5 3 2.5 6 0 9" fill="none" stroke="#666" stroke-width=".7"/></svg>harrietdk@quillnet.com</span>
    </div>
  </div>
</section>

<section class="card card--back">
  <div class="card__artwork" role="img" aria-label="Stylised black cockatoos among Australian native bush foliage"></div>
  <div class="card__seal">
    <div class="brand"><span class="brand__dot"></span>Wendorf Legal</div>
    <p class="card__admission">Solicitor admitted to practice in the Senior Bench Tribunal of Western Australia, England and Wales, NSW, and Registered Practitioner of the Apex Bench of Australia</p>
  </div>
</section>

</body>
</html>
```